Clever & creative business card needed for a pediatric dentist.

We need a business card for a pediatric dentist that is building a brand-new pediatric dental practice. He is funny, outgoing, and sociable, and he hopes to give his business card to dentists and pediatricians so that he can give them information of where to refer infants, children, and teenagers that need high quality and attainable dental care.

The name of the dental practice is Copper Fern Pediatric Dentistry. Logo design .png / .pdf/ .jpg are provided to aid in the design.

The dentist's last name is Tolvan (which sounds like "burger", as in "hamburger” or “cheeseburger"). Since it is pediatric practice, kudos will be given to designs that implement a little joke into the design - but hopefully in a small or hidden way (such as putting something like a cheeseburger on the back of the card, or hiding it an an abstract way).

Thank you!

Please make a design that incorporates colors. It should be fun! Not too serious. It does not have to follow the color scheme of the logos.

```html
<!DOCTYPE html>
<html lang="en">
<head>
<meta charset="utf-8">
<title>Copper Fern Pediatric Dentistry – Business Card</title>
<link rel="stylesheet" href="https://fonts.googleapis.com/css2?family=Montserrat:wght@400;500;600&display=swap">
<style>
  :root {
    --bg: #2b2b2b;
    --card: #161616;
    --green: #4cbb6c;
    --green-light: #8fd9a2;
    --white: #f2f2f2;
    --mark-grey: #3a3a3a;
  }
  html, body {
    margin: 0;
    width: 1200px;
    height: 900px;
    overflow: hidden;
    background: var(--bg);
    font-family: "Montserrat", Arial, sans-serif;
  }
  .stage {
    width: 1200px;
    height: 900px;
    display: flex;
    flex-direction: column;
    align-items: center;
    justify-content: center;
    gap: 44px;
  }
  .card {
    position: relative;
    width: 700px;
    height: 400px;
    background: var(--card);
    border-radius: 24px;
    border-bottom: 4px solid var(--green);
    box-shadow: 0 14px 30px rgba(0,0,0,0.45);
    box-sizing: border-box;
    overflow: hidden;
  }
  /* Front */
  .holder {
    position: absolute;
    left: 44px;
    top: 118px;
  }
  .holder-name {
    margin: 0;
    color: var(--green);
    font-size: 27px;
    font-weight: 500;
    letter-spacing: 0.5px;
    text-transform: uppercase;
  }
  .holder-title {
    margin: 2px 0 0;
    color: var(--white);
    font-size: 17px;
    font-weight: 400;
  }
  .divider {
    position: absolute;
    left: 44px;
    top: 208px;
    width: 560px;
    height: 1px;
    background: var(--green);
  }
  .contact-list {
    position: absolute;
    left: 44px;
    top: 228px;
    margin: 0;
    padding: 0;
    list-style: none;
    color: var(--white);
    font-size: 16px;
    line-height: 27px;
  }
  .contact-list li {
    display: flex;
    align-items: center;
    gap: 10px;
  }
  .contact-icon {
    width: 14px;
    height: 14px;
    flex: none;
  }
  .brand {
    position: absolute;
    right: 70px;
    top: 92px;
    text-align: right;
    display: flex;
    align-items: center;
    gap: 14px;
  }
  .brand-dot {
    width: 38px;
    height: 38px;
    border-radius: 50%;
    background: var(--green-light);
    flex: none;
  }
  .brand-name {
    margin: 0;
    color: var(--white);
    font-size: 34px;
    font-weight: 500;
    line-height: 1;
  }
  .brand-sub {
    margin: 8px 0 0;
    color: var(--white);
    font-size: 10px;
    font-weight: 500;
    letter-spacing: 5px;
    text-transform: uppercase;
  }
  .address {
    position: absolute;
    right: 96px;
    bottom: 34px;
    margin: 0;
    color: var(--white);
    font-size: 17px;
    font-style: normal;
    line-height: 24px;
    text-align: right;
  }
  /* Back */
  .back-mark {
    position: absolute;
    inset: 0;
    display: flex;
    align-items: center;
    justify-content: center;
    gap: 16px;
  }
  .back-dot {
    width: 56px;
    height: 56px;
    border-radius: 50%;
    background: var(--mark-grey);
  }
  .back-name {
    margin: 0;
    color: var(--mark-grey);
    font-size: 40px;
    font-weight: 500;
  }
</style>
</head>
<body>
<main class="stage">
  <section class="card card-front">
    <div class="holder">
      <h1 class="holder-name">Marcus Tolvan</h1>
      <p class="holder-title">President</p>
    </div>
    <div class="divider"></div>
    <ul class="contact-list">
      <li>
        <svg class="contact-icon" viewBox="0 0 16 16" aria-hidden="true"><path fill="#4cbb6c" d="M3.5 1.5l2.5 3-1.5 1.6c.8 1.8 2.2 3.2 4 4l1.6-1.5 3 2.5-1.4 2.3C7 13 3 9 1.2 2.9z"/></svg>
        949-555-0187
      </li>
      <li>
        <svg class="contact-icon" viewBox="0 0 16 16" aria-hidden="true"><rect x="1" y="3" width="14" height="10" rx="1" fill="#4cbb6c"/><path d="M1.5 3.8L8 9l6.5-5.2" stroke="#161616" stroke-width="1.3" fill="none"/></svg>
        marcust@copperfern.com
      </li>
      <li>
        <svg class="contact-icon" viewBox="0 0 16 16" aria-hidden="true"><circle cx="8" cy="8" r="7" fill="#4cbb6c"/><path d="M1 8h14M8 1c-3 3.5-3 10.5 0 14M8 1c3 3.5 3 10.5 0 14" stroke="#161616" stroke-width="1" fill="none"/></svg>
        www.copperfern.com
      </li>
    </ul>
    <div class="brand">
      <span class="brand-dot"></span>
      <div>
        <p class="brand-name">copper fern</p>
        <p class="brand-sub">Pediatric Dentistry</p>
      </div>
    </div>
    <address class="address">1780 Harbor Lane<br>Seacliff CA 92601</address>
  </section>

  <section class="card card-back" aria-label="Copper Fern Pediatric Dentistry">
    <div class="back-mark">
      <span class="back-dot"></span>
      <p class="back-name">copper fern</p>
    </div>
  </section>
</main>
</body>
</html>
```